Need professional Retail label design for new product VeltroGuard K7Q

I need a professional retail label designed for our product "VeltroGuard K7Q" Logo is attached for our company. My website is www.veltroguard-example.com you can visit our site and see what our product is about. This label will go on 5 gallon buckets and 1 gallon bottles. If you look at our competitors product website at
https://www.drizzleshieldusa-example.com/our-product/
you can get some kind of idea what i am looking for. I want the same content but better design than the drizzleshield design.
Colors should match our logo color pallet.
Colors
Designer to choose colors to be used in the design.
Requirements
Must have
- I would like a background that has blue water beading on the background. Maybe a blue water beading gradient background. Look at drizzleshield website for product label content and ideas.
- https://www.drizzleshieldusa-example.com/our-product/

```html
<!DOCTYPE html>
<html lang="en">
<head>
<meta charset="utf-8">
<title>VeltroGuard Retail Label</title>
<link rel="stylesheet" href="https://fonts.googleapis.com/css2?family=Open+Sans:wght@400;600&display=swap">
<style>
  :root {
    --page-bg: #f2f4f6;
    --label-top: #ffffff;
    --label-mist: #e3f1fb;
    --brand-blue: #2a7ab8;
    --mark-teal: #1aa7c9;
    --ink: #1d1d1d;
    --accent-orange: #d9661f;
    --water-light: #5cb7ea;
    --water-mid: #1f86cf;
    --water-deep: #0b4f92;
    --roof-tile: #c46a4a;
    --stone-slate: #3b3f45;
    --paver-brick: #9a5a4c;
    --concrete-grey: #8b8d8c;
  }
  * { box-sizing: border-box; margin: 0; padding: 0; }
  html, body { width: 1200px; height: 1200px; overflow: hidden; }
  body {
    background: var(--page-bg);
    font-family: "Open Sans", Arial, sans-serif;
    color: var(--ink);
    position: relative;
  }
  .label {
    position: absolute;
    left: 0; top: 300px;
    width: 1200px; height: 600px;
    overflow: hidden;
    background: radial-gradient(ellipse at 30% 20%, var(--label-top) 0%, var(--label-mist) 100%);
  }
  .water-band {
    position: absolute;
    left: 0; top: 0;
    width: 1200px; height: 600px;
  }
  .brand {
    position: absolute;
    left: 50px; top: 40px;
    display: flex; align-items: center; gap: 22px;
  }
  .brand-mark {
    width: 78px; height: 78px; border-radius: 50%;
    background: var(--mark-teal);
  }
  .brand-name {
    font-size: 66px; font-weight: 600;
    color: var(--brand-blue);
    letter-spacing: 1px;
  }
  .surfaces {
    position: absolute;
    left: 55px; top: 160px;
    display: flex; gap: 22px;
  }
  .surface { width: 126px; text-align: center; }
  .surface-photo { width: 126px; height: 112px; }
  .surface-photo.roof { background: linear-gradient(160deg, #d8866a, var(--roof-tile)); }
  .surface-photo.stone { background: linear-gradient(160deg, #555a61, var(--stone-slate)); }
  .surface-photo.pavers { background: linear-gradient(160deg, #7f8a5a 0%, var(--paver-brick) 55%); }
  .surface-photo.concrete { background: linear-gradient(160deg, #a7a9a8, var(--concrete-grey)); }
  .surface-caption { font-size: 20px; margin-top: 4px; }
  .product-copy {
    position: absolute;
    left: 700px; top: 55px;
    width: 460px;
    font-size: 15.5px; line-height: 1.22;
  }
  .product-copy p + p { margin-top: 16px; }
</style>
</head>
<body>
  <section class="label">
    <svg class="water-band" viewBox="0 0 1200 600" width="1200" height="600">
      <defs>
        <linearGradient id="waterFill" x1="0" y1="0" x2="0" y2="1">
          <stop offset="0" stop-color="var(--water-light)"/>
          <stop offset="0.5" stop-color="var(--water-mid)"/>
          <stop offset="1" stop-color="var(--water-deep)"/>
        </linearGradient>
      </defs>
      <path role="img" aria-label="Blue surface covered in beading water droplets"
            d="M0 380 C250 430 450 450 700 440 C900 432 1050 420 1200 420 L1200 600 L0 600 Z"
            fill="url(#waterFill)"/>
      <path d="M0 374 C250 424 450 444 700 434 C900 426 1050 414 1200 414"
            fill="none" stroke="var(--accent-orange)" stroke-width="5"/>
      <path d="M0 364 C250 414 450 434 700 424 C900 416 1050 404 1200 404"
            fill="none" stroke="#ffffff" stroke-width="4"/>
    </svg>

    <header class="brand">
      <span class="brand-mark"></span>
      <span class="brand-name">VeltroGuard</span>
    </header>

    <div class="surfaces">
      <figure class="surface">
        <div class="surface-photo roof" role="img" aria-label="Terracotta tile roof"></div>
        <figcaption class="surface-caption">Tile Roof</figcaption>
      </figure>
      <figure class="surface">
        <div class="surface-photo stone" role="img" aria-label="Dark stacked stone wall"></div>
        <figcaption class="surface-caption">Stone</figcaption>
      </figure>
      <figure class="surface">
        <div class="surface-photo pavers" role="img" aria-label="Brick paver walkway"></div>
        <figcaption class="surface-caption">Pavers</figcaption>
      </figure>
      <figure class="surface">
        <div class="surface-photo concrete" role="img" aria-label="Grey aggregate concrete"></div>
        <figcaption class="surface-caption">Concrete</figcaption>
      </figure>
    </div>

    <div class="product-copy">
      <p>Lorem ipsum, or lipsum as it is sometimes known, is dummy text used in laying out print, graphic or web designs. The passage is attributed to an unknown typesetter in the 15th century who is thought to have scrambled parts of Varrenus's De Finibus Bonorum et Malorum for use in a type specimen book. It usually begins with:</p>
      <p>Lorem ipsum dolor sit amet, consectetur adipiscing elit, sed do eiusmod tempor incididunt ut labore et dolore magna aliqua.”</p>
      <p>The purpose of lorem ipsum is to create a natural looking block of text (sentence, paragraph, page, etc.) that doesn't distract from the layout. A practice not without controversy, laying out pages with</p>
    </div>
  </section>
</body>
</html>
```